Modern Lawfirm Business Card Design

We're looking for a business card to incorporate the newly created logo we had made.

Ideally looking for a law firm business card demonstrating, modern, minimalist, strong/bold design.

I'm open to any design honestly, but nothing "flashy".

Target Market(s)

Immigration law, family immigration, humanitarian, general legal

Industry/Entity Type

Law Firm

Contact Information for Business Card

Please use dummy information, name, street address, city, state, phone number, email, website.

Font styles to use
Serif
Sans Serif

Requirements
Must have
• Please use dummy information, name, street address, city, state, phone number, email, website.

```html
<!DOCTYPE html>
<html lang="en">
<head>
<meta charset="utf-8">
<title>Calderon Immigration Law – Business Card</title>
<link rel="stylesheet" href="https://fonts.googleapis.com/css2?family=Crimson+Text:wght@400;600&display=swap">
<style>
  :root {
    --bg: #e9e7e3;
    --navy: #1d5a96;
    --navy-deep: #144a80;
    --paper: #ffffff;
    --taupe: #8f8a74;
    --ink: #4a4a4a;
    --rule: #9a9a9a;
  }
  * { margin: 0; padding: 0; box-sizing: border-box; }
  html, body { width: 1200px; height: 843px; overflow: hidden; }
  body {
    background: var(--bg);
    font-family: "Crimson Text", Georgia, serif;
    display: flex;
    align-items: center;
    justify-content: center;
    gap: 60px;
  }
  .card {
    position: relative;
    width: 520px;
    height: 298px;
    overflow: hidden;
    box-shadow: 0 6px 18px rgba(0,0,0,.18);
  }
  .card-front { background: var(--paper); }
  .card-back { background: var(--navy); color: var(--paper); }

  .front-wave { position: absolute; inset: 0; width: 100%; height: 100%; }
  .front-wave .band { fill: var(--navy); }
  .front-wave .swoosh { fill: var(--taupe); }

  .brand-name {
    position: absolute;
    left: 34px;
    top: 62px;
    color: var(--navy);
    font-weight: 600;
    font-size: 26px;
    line-height: 1;
    letter-spacing: 1px;
  }
  .brand-name .brand-sub {
    display: block;
    font-size: 11px;
    letter-spacing: 4px;
    margin-top: 5px;
  }

  .divider {
    position: absolute;
    left: 262px;
    top: 66px;
    width: 1px;
    height: 112px;
    background: var(--rule);
  }

  .contact {
    position: absolute;
    left: 282px;
    top: 70px;
    color: var(--ink);
    font-size: 13px;
    line-height: 1.25;
  }
  .contact .person-name { color: var(--navy); font-size: 20px; line-height: 1.1; }
  .contact .credentials { font-size: 14px; margin-bottom: 10px; }
  .contact .line { display: flex; align-items: center; gap: 8px; margin-bottom: 4px; }
  .contact .icon { width: 12px; height: 12px; fill: var(--ink); flex: none; }
  .contact .address { margin-top: 6px; }

  .back-content {
    position: absolute;
    inset: 0;
    display: flex;
    flex-direction: column;
    align-items: center;
    justify-content: center;
    text-align: center;
  }
  .back-content .brand-name {
    position: static;
    color: var(--paper);
    font-size: 40px;
  }
  .back-content .brand-name .brand-sub { font-size: 15px; letter-spacing: 6px; margin-top: 8px; }
  .website { margin-top: 36px; font-size: 16px; }
</style>
</head>
<body>
  <section class="card card-front">
    <svg class="front-wave" viewBox="0 0 520 298" preserveAspectRatio="none" aria-hidden="true">
      <path class="swoosh" d="M0,110 C90,118 170,140 230,178 C170,150 90,130 0,122 Z"/>
      <path class="band" d="M0,150 C190,180 390,205 450,298 L0,298 Z"/>
    </svg>

    <div class="brand-name">CALDERON<span class="brand-sub">IMMIGRATION LAW</span></div>
    <div class="divider"></div>

    <div class="contact">
      <div class="person-name">Daniel Calderon</div>
      <div class="credentials">J.D., LL.M.</div>
      <div class="line">
        <svg class="icon" viewBox="0 0 24 24"><path d="M6.6 10.8a15 15 0 0 0 6.6 6.6l2.2-2.2c.3-.3.7-.4 1-.2 1.1.4 2.3.6 3.6.6.6 0 1 .4 1 1V20c0 .6-.4 1-1 1A17 17 0 0 1 3 4c0-.6.4-1 1-1h3.5c.6 0 1 .4 1 1 0 1.3.2 2.5.6 3.6.1.3 0 .7-.2 1z"/></svg>
        <span>123 4567 8910</span>
      </div>
      <div class="line">
        <svg class="icon" viewBox="0 0 24 24"><path d="M2 5h20v14H2z M4 7v.4l8 5.2 8-5.2V7z" fill-rule="evenodd"/></svg>
        <span>info@calderonlaw.com</span>
      </div>
      <div class="address">14 Harlow Street,<br>Westbrook NSW 2071</div>
    </div>
  </section>

  <section class="card card-back">
    <div class="back-content">
      <div class="brand-name">CALDERON<span class="brand-sub">IMMIGRATION LAW</span></div>
      <div class="website">www.calderonlaw.com</div>
    </div>
  </section>
</body>
</html>
```